Need a flyer to leave behind when visiting clients or at shows

Glossy colorful tri-fold flyer with the same information that is on my web site www.palverdmks.com. I am open to a little modern or creative take on the typical brochure. I created the web site so I can provide any raw files needed from it. I would also like the ability to edit this flyer in the future in Adobe Photoshop Elements

```html
<!DOCTYPE html>
<html lang="en">
<head>
<meta charset="utf-8">
<title>Palverd Health Solutions – Tri-fold Brochure</title>
<link href="https://fonts.googleapis.com/css2?family=Oswald:wght@300;400&family=Montserrat:wght@300;400;500;600;700&family=Open+Sans:wght@400&display=swap" rel="stylesheet">
<style>
  :root{
    --stage:#FFE800;
    --label:#6A3FA0;
    --brand:#4B2C8C;
    --brand-deep:#3A1F6E;
    --ink:#1b1b1b;
    --paper:#ffffff;
    --night:#141414;
  }
  *{box-sizing:border-box;margin:0;padding:0}
  html,body{width:1200px;height:1200px;overflow:hidden;background:var(--stage)}
  body{position:relative;font-family:"Montserrat",Arial,sans-serif;color:var(--ink)}
  .side-tag{position:absolute;left:62px;width:254px;height:73px}
  .side-tag svg{position:absolute;inset:0}
  .side-tag span{position:absolute;left:0;width:220px;top:0;height:73px;line-height:73px;text-align:center;
    font-family:"Open Sans",Arial,sans-serif;font-size:56px;color:#fff}
  .side-tag--front{top:262px}
  .side-tag--back{top:855px}

  .sheet{position:absolute;background:var(--paper);overflow:hidden;box-shadow:0 6px 18px rgba(0,0,0,.18)}
  .sheet--front{left:367px;top:28px;width:715px;height:556px}
  .sheet--back{left:369px;top:626px;width:711px;height:554px}
  .abs{position:absolute}
  .block{position:absolute;background:var(--brand)}
  .photo{position:absolute}

  /* front */
  .values-title{left:29px;top:322px;font-family:"Oswald",sans-serif;font-weight:300;font-size:25px;color:var(--brand-deep);letter-spacing:.3px}
  .value{position:absolute;left:30px;display:flex;align-items:center;gap:9px}
  .value__icon{width:50px;height:37px;background:var(--label);display:flex;align-items:center;justify-content:center}
  .value__label{font-size:10.5px;color:var(--brand);font-weight:500;line-height:1.25}
  .team-title{left:261px;top:32px;font-family:"Oswald",sans-serif;font-weight:300;font-size:22px;color:#111}
  .bio{left:258px;top:71px;width:196px;font-size:6.2px;line-height:11.1px;text-align:justify;color:#222}
  .bio__card{float:left;width:92px;margin-right:6px;height:186px}
  .bio__headshot{width:87px;height:107px;background:linear-gradient(180deg,#b9b9b9,#8a8a8a);border-right:2px solid var(--brand);border-bottom:2px solid var(--brand)}
  .bio__name{font-size:14px;color:var(--brand);margin-top:7px}
  .bio__meta{font-size:9px;color:var(--brand);margin-top:4px;line-height:13px}
  .contact{left:258px;top:302px;width:196px;height:75px;border:1.5px solid var(--brand);padding:9px 0 0 30px;font-size:10.3px;line-height:19.5px;color:#111}
  .contact div{display:flex;align-items:center;gap:5px}
  .promo-text{left:490px;top:193px;color:#fff;line-height:1.05}
  .promo-text .l1{font-size:24px;font-weight:400;letter-spacing:.6px}
  .promo-text .l2{font-size:26px;font-weight:700}
  .promo-text .l3{font-size:18px;font-weight:700;margin-top:2px}
  .promo-text .l4{font-size:14px;font-weight:700;margin-top:4px}
  .brand-name{left:487px;top:412px;width:206px;text-align:center;color:var(--brand);font-weight:700;font-size:24px;line-height:1.15;letter-spacing:.5px}
  .brand-name small{display:block;font-size:24px}
  .site{left:517px;top:513px;font-size:13px;display:flex;gap:5px;align-items:center;color:#111}

  /* back */
  .obj-title{left:28px;top:282px;font-family:"Oswald",sans-serif;font-weight:300;font-size:33px;line-height:36px;color:var(--brand-deep);letter-spacing:.5px}
  .obj{position:absolute;left:19px;display:flex;align-items:center;gap:7px;font-size:10.3px;line-height:12px;color:#222}
  .obj__icon{width:36px;height:36px;border-radius:50%;background:var(--brand-deep);flex:none;display:flex;align-items:center;justify-content:center}
  .services-title{left:265px;top:58px;color:#fff;line-height:1}
  .services-title .thin{font-size:40px;font-weight:300;display:block}
  .services-title .bold{font-size:32px;font-weight:700;display:block}
  .services-box{left:262px;top:148px;width:197px;height:314px;background:rgba(10,10,10,.82)}
  .services-copy{left:279px;top:162px;width:160px;font-size:8px;line-height:14px;color:#ddd;text-align:justify}
  .services-sub{left:279px;top:294px;font-size:12.6px;color:#fff}
  .services-list{left:276px;top:320px;list-style:none;font-size:7.3px;color:#eee}
  .services-list li{height:18.6px;display:flex;gap:4px;align-items:center}
  .about-title{left:491px;top:28px;font-family:"Oswald",sans-serif;font-weight:300;font-size:29px;color:var(--brand-deep)}
  .about{left:491px;top:66px;width:210px}
  .about h3{font-size:13.5px;font-weight:400;margin-top:3px}
  .about p{font-size:7.6px;font-weight:600;line-height:16.5px;margin-bottom:2px}
</style>
</head>
<body>

<div class="side-tag side-tag--front">
  <svg width="254" height="73"><polygon points="0,0 208,0 254,36.5 208,73 0,73" fill="var(--label)"/></svg>
  <span>Fornt</span>
</div>
<div class="side-tag side-tag--back">
  <svg width="254" height="73"><polygon points="0,0 208,0 254,36.5 208,73 0,73" fill="var(--label)"/></svg>
  <span>Back</span>
</div>

<section class="sheet sheet--front">
  <div class="block" style="left:0;top:26px;width:251px;height:286px"></div>
  <div class="photo" role="img" aria-label="Close-up of a screen showing the word Security with a pointing cursor" style="left:0;top:56px;width:234px;height:256px;background:radial-gradient(circle at 45% 45%,#2e3a44,#111 75%)"></div>

  <h2 class="abs values-title">OUR CORE VALUES</h2>
  <div class="value" style="top:357px"><div class="value__icon"><svg width="26" height="26" viewBox="0 0 26 26" fill="none" stroke="#fff" stroke-width="1.5"><circle cx="13" cy="13" r="11"/><circle cx="13" cy="10" r="3"/><path d="M7 19c1-3 4-4 6-4s5 1 6 4"/></svg></div><span class="value__label">CLIENT FOCUSED</span></div>
  <div class="value" style="top:405px"><div class="value__icon"><svg width="28" height="24" viewBox="0 0 28 24" fill="none" stroke="#fff" stroke-width="1.5"><circle cx="7" cy="5" r="2.5"/><circle cx="21" cy="5" r="2.5"/><path d="M3 22v-9h6v9M19 22v-9h6v9M9 14h10M14 14v8"/></svg></div><span class="value__label">ACCOUNTABILITY</span></div>
  <div class="value" style="top:454px"><div class="value__icon"><svg width="26" height="26" viewBox="0 0 26 26" fill="none" stroke="#fff" stroke-width="1.5"><path d="M13 4v18M6 8h14M6 8l-3 7h6zM20 8l-3 7h6zM9 22h8"/></svg></div><span class="value__label">INTEGRITY</span></div>
  <div class="value" style="top:502px"><div class="value__icon"><svg width="26" height="26" viewBox="0 0 26 26" fill="#fff"><rect x="3" y="18" width="4" height="6"/><rect x="9" y="15" width="4" height="9"/><rect x="15" y="12" width="4" height="12"/><rect x="21" y="8" width="4" height="16"/><circle cx="11" cy="4" r="2"/></svg></div><span class="value__label">PROFESSIONAL<br>DEVELOPMENT</span></div>

  <h2 class="abs team-title">Our Leadership Team</h2>
  <div class="abs bio">
    <div class="bio__card">
      <div class="bio__headshot" role="img" aria-label="Portrait of the company president"></div>
      <div class="bio__name">Dana Mercer</div>
      <div class="bio__meta">MHA, MBA, CHCIO<br>President &amp; CEO</div>
    </div>
    Dana is the founder and CEO of Palverd Health Solutions. She has been working in the technology industry for over 25 years with extensive experience in healthcare IT. Dana has held multiple roles including Chief Information Officer, Chief Information Security Officer, and the executive sponsor of multiple electronic health record (EHR) implementations. She has created and nurtured numerous successful IT departments and built strong relationships with leadership teams. Dana holds a Master's in Business Administration and a Master's in Healthcare Administration, and is certified with the Guild of Health Information Leaders (GHIL).
  </div>

  <div class="abs contact">
    <div><svg width="9" height="9" viewBox="0 0 10 10"><path d="M2 0l2 2.5-1.2 1.3a6 6 0 0 0 3.4 3.4L7.5 6 10 8l-1.5 2C4 10 0 6 0 1.5z" fill="var(--brand)"/></svg>555-014-2290</div>
    <div><svg width="10" height="8" viewBox="0 0 10 8"><rect width="10" height="8" fill="var(--brand)"/><path d="M0 0l5 4 5-4" stroke="#fff" fill="none"/></svg>dmercer@palverdmks.com</div>
    <div><svg width="10" height="10" viewBox="0 0 10 10"><circle cx="5" cy="5" r="4.5" fill="none" stroke="var(--brand)"/><path d="M3 2c2 1 1 3 3 3s1 3 0 4" stroke="var(--brand)" fill="none"/></svg>www.palverdmks.com</div>
  </div>

  <div class="photo" role="img" aria-label="Team members giving a high five over an office desk" style="left:233px;top:380px;width:232px;height:176px;background:linear-gradient(160deg,#3c4a5c,#1d2430 50%,#6a5a4c)"></div>

  <div class="block" style="left:561px;top:234px;width:154px;height:152px"></div>
  <div class="photo" role="img" aria-label="Presenter pointing at charts in a meeting room" style="left:487px;top:50px;width:198px;height:294px;background:linear-gradient(180deg,#3a3a3a,#1b1b1b 60%,#6b5240)"></div>
  <div class="abs promo-text">
    <div class="l1">Increasing</div>
    <div class="l2">The Value &amp;</div>
    <div class="l3">Security of Your</div>
    <div class="l4">Technology Resources</div>
  </div>

  <div class="abs brand-name">PALVERD<small>HEALTH SOLUTIONS</small></div>
  <div class="abs site"><svg width="13" height="13" viewBox="0 0 10 10"><circle cx="5" cy="5" r="4.5" fill="none" stroke="#111"/><path d="M3 2c2 1 1 3 3 3s1 3 0 4" stroke="#111" fill="none"/></svg>www.palverdmks.com</div>
</section>

<section class="sheet sheet--back">
  <div class="block" style="left:0;top:0;width:186px;height:182px"></div>
  <div class="photo" role="img" aria-label="Overhead view of a team working at a wooden desk with laptops" style="left:29px;top:46px;width:214px;height:213px;background:linear-gradient(135deg,#c9a57c,#a98259 50%,#8b8b8b)"></div>

  <h2 class="abs obj-title">OUR PRIMARY<br>OBJECTIVES</h2>
  <div class="obj" style="top:376px"><div class="obj__icon"><svg width="20" height="20" viewBox="0 0 20 20" fill="#fff"><circle cx="10" cy="6" r="3"/><circle cx="4" cy="9" r="2"/><circle cx="16" cy="9" r="2"/><path d="M4 17c0-4 3-6 6-6s6 2 6 6z"/></svg></div><span>Understand and exceed client<br>expectations</span></div>
  <div class="obj" style="top:424px"><div class="obj__icon"><svg width="22" height="16" viewBox="0 0 22 16" fill="none" stroke="#fff" stroke-width="1.6"><path d="M1 5l5-3 5 3 5-3 5 3M4 7l6 6 2-1M11 5l-3 3 2 2 4-2 4 2"/></svg></div><span>Committed to be a partner, not<br>vendo</span></div>
  <div class="obj" style="top:472px"><div class="obj__icon"><svg width="22" height="22" viewBox="0 0 22 22" fill="none" stroke="#fff" stroke-width="1.3"><circle cx="11" cy="11" r="4"/><circle cx="11" cy="3" r="1.6"/><circle cx="11" cy="19" r="1.6"/><circle cx="3" cy="11" r="1.6"/><circle cx="19" cy="11" r="1.6"/><path d="M11 5v2M11 15v2M5 11h2M15 11h2"/></svg></div><span>Provide simplified change<br>management expertise</span></div>

  <div class="photo" role="img" aria-label="Dark photo of hands using a laptop keyboard" style="left:243px;top:21px;width:231px;height:505px;background:linear-gradient(170deg,#2a2a2a,#111 55%,#3a2e26)"></div>
  <div class="abs services-title"><span class="thin">Our</span><span class="bold">Services</span></div>
  <div class="abs services-box"></div>
  <p class="abs services-copy">We understand different organizations have different needs. Palverd HCS strives to assist your organization by bringing solutions that are easy to understand and allow the client to track success. We provide solutions based on the client's needs and desires.</p>
  <h3 class="abs services-sub" style="font-weight:400">Information Technology</h3>
  <ul class="abs services-list">
    <li><span style="color:#8e6bd6">✓</span>CIO or IT Director Services</li>
    <li><span style="color:#8e6bd6">✓</span>CISO or Information Security Officer</li>
    <li><span style="color:#8e6bd6">✓</span>Comprehensive ePHI Risk Assessments</li>
    <li><span style="color:#8e6bd6">✓</span>IT Department Evaluation</li>
    <li><span style="color:#8e6bd6">✓</span>Policy Management and Consulting</li>
    <li><span style="color:#8e6bd6">✓</span>On-going IT department support</li>
  </ul>

  <h2 class="abs about-title">About Us</h2>
  <div class="abs about">
    <h3>Our Mission</h3>
    <p>Partner with clients to increase the value and security of their technology tools.</p>
    <h3>Our Goal</h3>
    <p>Become the premiere consulting company for Information Technology in the long term care industry.</p>
    <h3>Our Leaders</h3>
    <p>Dana Mercer, MHA, MBA, CHCIO</p>
  </div>

  <div class="block" style="left:569px;top:322px;width:142px;height:232px"></div>
  <div class="photo" role="img" aria-label="Hand touching a blue hexagon interface labelled IT, Data and Computer" style="left:474px;top:262px;width:191px;height:198px;background:radial-gradient(circle at 70% 30%,#3f7fd0,#1f4a86 55%,#13294d)"></div>
</section>

</body>
</html>
```